Homepage Website Design for luxury picnic company

We need a homepage designed for a luxury picnic business to match our updated branding/logo which we're currently completing on ArtGatherly with another competition. Please see attached logo/colour example to use for now.

PLEASE NOTE: We are only after graphic design concepts as part of this competition. I will get another developer to actually code the website.

It is important that this website is very elegant/luxurious and stands out from a visual perspective. The images really need to match the content/sections also. The new branding colours are silver with a dark background. Please create the new website homepage to match these colours/branding.

Please create as many concepts as possible and then I will provide feedback from there

The website content including sections is here https://pages.velmoranote.com/doc/d/7kRtWq2mLp9XcVb4Hn8Js3Yd6Fg1Za5Qe0Uo2Ti/edit?mode=share

Images to use are located here https://vault.trenquilbox.com/vault/dirs/5HmQzR2-NcWy8Kp41-7VbLdTsXoeFj?mode=share and there is also lots of videos at this link which you can screenshot images out of if needed https://www.stashquarry.com/sh/k827trwm3hdz4/AACvnRt2Lm8WqPe5Xu9JdsYk?dl=0

Any questions please contact me

```html
<!DOCTYPE html>
<html lang="en">
<head>
<meta charset="utf-8">
<title>Velora – Luxury Picnics</title>
<link href="https://fonts.googleapis.com/css2?family=Libre+Caslon+Text:wght@400;700&family=Montserrat:wght@300;400&display=swap" rel="stylesheet">
<style>
:root{
  --ink:#0a0d17;
  --silver:#8e9096;
  --silver-light:#c8c9cc;
  --paper:#ffffff;
  --mist:#f7f7f7;
  --text:#2b2d33;
  --rule:#9a9ca2;
  --sky-blue:#1aa6e0;
  --press:#7b7d82;
}
*{margin:0;padding:0;box-sizing:border-box}
html,body{width:1200px;height:3126px;overflow:hidden}
body{position:relative;background:var(--paper);font-family:'Montserrat',sans-serif;color:var(--text)}
.abs{position:absolute}
.serif{font-family:'Libre Caslon Text',serif}

/* hero */
.hero{left:0;top:0;width:1200px;height:600px;background:linear-gradient(180deg,#3d4556 0%,#2c3240 30%,#3a3530 60%,#4a3a36 100%)}
.hero-shade{left:0;top:0;width:1200px;height:600px;background:rgba(10,13,23,.25)}
.brand{left:113px;top:22px;width:45px;height:45px;background:var(--ink);color:#fff;font-family:'Libre Caslon Text',serif;font-size:10px;display:flex;align-items:center;justify-content:center}
.hero-title{left:0;top:216px;width:1200px;text-align:center;color:#fff;font-size:36px;letter-spacing:1px}
.hero-sub{left:0;top:270px;width:1200px;text-align:center;color:#fff;font-size:18px}
.hero-btn{left:506px;top:330px;width:187px;height:44px;border:1px solid #fff;color:#fff;font-family:'Libre Caslon Text',serif;font-size:11px;display:flex;align-items:center;justify-content:center;letter-spacing:.5px}
.badge{left:945px;top:163px;width:76px;height:76px;border-radius:50%;background:var(--sky-blue);border:4px solid #fff}

/* labels */
.rule{height:1px;width:74px;background:var(--rule)}
.label{font-family:'Libre Caslon Text',serif;font-size:17px;letter-spacing:7px;color:var(--silver)}

/* as seen on */
.press{left:0;top:600px;width:1200px;height:113px;background:var(--paper)}
.press-name{top:652px;width:140px;text-align:center;font-family:'Montserrat',sans-serif;font-weight:400;font-size:23px;color:var(--press)}

/* selling points */
.points{left:0;top:713px;width:1200px;height:832px;background:var(--mist)}
.point-photo{width:225px;height:299px}
.point-card{width:225px;height:362px;background:var(--paper);text-align:center;padding:33px 16px 0}
.point-card h3{font-family:'Libre Caslon Text',serif;font-weight:400;font-size:14px;letter-spacing:5px;color:var(--silver);margin-bottom:14px}
.point-card p{font-size:10px;line-height:22.5px;letter-spacing:2.5px;color:var(--text);font-weight:300}

/* about */
.about{left:0;top:1545px;width:1200px;height:600px;background:var(--ink)}
.about-title{left:113px;top:1735px;width:420px;color:#fff;font-size:36px;line-height:54px}
.video{left:600px;top:1621px;width:600px;height:449px;background:linear-gradient(180deg,#4a5366 0%,#5d6475 45%,#3c4a66 70%,#28314a 100%)}

/* pricing */
.pricing{left:0;top:2145px;width:1200px;height:981px;background:linear-gradient(180deg,#eceef1 0%,#f1f1f2 60%,#ebe9ea 100%)}
.plan{width:300px;height:465px;background:var(--paper);text-align:center;padding-top:54px}
.plan h3{font-family:'Libre Caslon Text',serif;font-weight:400;font-size:14px;letter-spacing:4.5px;color:var(--silver)}
.plan .price{font-family:'Libre Caslon Text',serif;font-size:44px;color:var(--ink);margin:24px 0 18px}
.plan .price small{font-size:10px;font-family:'Montserrat',sans-serif}
.plan ul{list-style:none;font-size:8.5px;color:var(--text);padding:0 34px}
.plan li{line-height:12px;margin-bottom:18px}
.pay-title{left:0;top:2827px;width:1200px;text-align:center;font-family:'Libre Caslon Text',serif;font-size:14px;letter-spacing:5px;color:var(--text)}
.pay-text{left:175px;width:850px;text-align:center;font-family:'Libre Caslon Text',serif;font-size:14.5px;line-height:22.7px;letter-spacing:4.2px;color:var(--text)}
</style>
</head>
<body>

<section class="hero abs" role="img" aria-label="Photo of a couple sharing a drink at a clifftop picnic above a mountain valley at dusk"></section>
<div class="hero-shade abs"></div>
<div class="brand abs">Velora</div>
<h1 class="hero-title abs serif" style="font-weight:400">SHARE AN UNFORGETTABLE MOMENT</h1>
<p class="hero-sub abs serif">Luxury picnics at breathtaking locations</p>
<a class="hero-btn abs">BOOK YOUR PICNIC</a>
<div class="badge abs" aria-label="Safety certification badge"></div>

<section class="press abs"></section>
<div class="rule abs" style="left:113px;top:639px"></div>
<div class="label abs" style="left:113px;top:659px">AS SEEN ON</div>
<div class="press-name abs" style="left:619px">Lumagift</div>
<div class="press-name abs" style="left:782px">Lumagift</div>
<div class="press-name abs" style="left:946px">Lumagift</div>

<section class="points abs"></section>
<div class="rule abs" style="left:113px;top:787px"></div>
<div class="label abs" style="left:113px;top:806px">KEY SELLING POINTS</div>

<div class="point-photo abs" style="left:113px;top:882px;background:linear-gradient(160deg,#5d6a4a,#b88a8a 60%,#7a6060)" role="img" aria-label="Photo of friends laughing together on a picnic rug among greenery"></div>
<div class="point-card abs" style="left:188px;top:1107px"><h3>BLISS</h3><p>We enable you to enjoy true quality time with your partner, friends or family. We do this by creating the perfect atmosphere to celebrate a special moment in your life or to simply spoil yourself!</p></div>

<div class="point-photo abs" style="left:450px;top:882px;background:linear-gradient(180deg,#4a5a78,#8a8a7a 45%,#6b6a66 75%,#3e4a3a)" role="img" aria-label="Photo of a couple seated on a rock ledge looking out over the mountains"></div>
<div class="point-card abs" style="left:525px;top:1107px"><h3>UNWIND</h3><p>Let us do everything for you so you can enjoy a stress free experience. You will also discover the Blue Mountains like you never have before! Each of our picnic spots are absolutely stunning and also very private.</p></div>

<div class="point-photo abs" style="left:787px;top:882px;background:linear-gradient(180deg,#6a7a55,#6a3a30 50%,#8a2a30)" role="img" aria-label="Photo of bottled drinks and glassware on a wooden board over a red rug"></div>
<div class="point-card abs" style="left:862px;top:1107px"><h3>INDULGE</h3><p>Our delicious picnics will have your mouth watering! You can design your own picnic by choosing from our extensive menu along with 2 choices of your favourite alcoholic &amp; non-alcoholic beverages. We cater for all dietary requirements and also have a BYO option.</p></div>

<section class="about abs"></section>
<div class="rule abs" style="left:113px;top:1620px;background:#6d7078"></div>
<div class="label abs" style="left:113px;top:1639px;color:var(--silver-light)">ABOUT HIGHRIDGE PICNICS</div>
<h2 class="about-title abs serif" style="font-weight:400">DISCOVER EXACTLY HOW OUR PICNICS WORK IN ONLY 90 SECONDS!</h2>
<div class="video abs" role="img" aria-label="Video still of a couple embracing on a clifftop at dusk"></div>
<svg class="abs" style="left:861px;top:1807px" width="76" height="76" viewBox="0 0 76 76" aria-label="Play video">
  <circle cx="38" cy="38" r="36" fill="none" stroke="#fff" stroke-width="3"/>
  <path d="M29 22 L55 38 L29 54 Z" fill="none" stroke="#fff" stroke-width="3" stroke-linejoin="round"/>
</svg>

<section class="pricing abs" role="img" aria-label="Faded background photo of a picnic setting among trees"></section>
<div class="rule abs" style="left:113px;top:2221px"></div>
<div class="label abs" style="left:113px;top:2239px">PRICING</div>

<div class="plan abs" style="left:113px;top:2291px">
  <h3>BYO PICNIC</h3>
  <div class="price">$200<small> + GST</small></div>
  <ul>
    <li>Hire, Transport and Setup of Picnic Equipment</li>
    <li>Directions to 'Secret' Location,</li>
    <li>2 Hour Picnic</li>
    <li>Cleaning and Pack up</li>
    <li>Still or Sparkling Water Cooled on Ice with Glassware</li>
    <li>BYO additional food &amp; beverages</li>
  </ul>
</div>
<div class="plan abs" style="left:450px;top:2291px">
  <h3>GOURMET PICNIC</h3>
  <div class="price">$350<small> + GST</small></div>
  <ul>
    <li>Everything in the BYO Picnic</li>
    <li>Design your own Gourmet Grazing Platter</li>
    <li>Choose 2 types of Complimentary Beverages</li>
    <li>Delivery of the Food and Beverages to the Picnic Spot</li>
    <li>Matching Glassware and Cutlery</li>
  </ul>
</div>
<div class="plan abs" style="left:787px;top:2291px">
  <h3>PROPOSAL PICNIC</h3>
  <div class="price">$350<small> + GST</small></div>
  <ul>
    <li>1 on 1 VIP Treatment</li>
    <li>Suggestions for Accommodation</li>
    <li>Activites</li>
    <li>Restaurants</li>
    <li>Assistance with any requests</li>
    <li>Directions to Location prior to the Picnic</li>
    <li>Help with Organising Photography</li>
    <li>Anything else needed for a successful proposal!</li>
  </ul>
</div>

<div class="pay-title abs">PAYMENT PLANS AVAILABLE</div>
<p class="pay-text abs" style="top:2872px">To secure your booking, all we need is a $100 + GST deposit. We offer custom payment plans at no extra cost. Once we receive your deposit we will be in touch to organise the best arrangements with you and just need you to have paid in full prior to the picnic.</p>
<p class="pay-text abs" style="top:2984px">If you prefer, you can still pay upfront to save the extra mucking around with a payment plan but it makes no difference from our end so please do whatever is best for you.</p>

</body>
</html>
```